Wordpress Lifestyle Blog

Just to be clear - I have the domain and the wordpress site (which is messy). I need someone to help me complete a simple blog design and then go into the existing wordpress site, and get rid of all the existing rubbish and set up the templates please. If we progress with design can we please be clear about additional costs upfront which, of course, I appreciate is the case.

Need a lifestyle blog. It is called brightyearsahead.com. Aimed at the older woman but needs to look fresh and young, not old fashioned. Navigation will be Home, Fashion, Feelings, Fitness, Contact. I have a logo but not sure it will work at the moment so happy with stylised words.Will have social media links.

Need homepage (not overly long) to have a main slider for pics/videos. Then the three category boxes underneath linking through to 2nd level pages containing blogs for that category and then the actual blog page. Happy to be led by expertise if this is not gonna work.

Am really looking for something clean and fresh like a Marwyn type approach to be honest.

If you need any further direction please just ask - once design chosen I am looking to move quickly.

Thank you so much for looking at this brief

Target Market(s)

Women, 40 - 60 age group but with a younger outlook

Number of Pages Required

3 page

Colors

Designer to choose colors to be used in the design.

Requirements
Must have
• Reflect youth, fun, bright
• Lift easily into a wordpress format
Should not have
• Old, staid, frumpy,dark

```html
<!DOCTYPE html>
<html lang="en">
<head>
<meta charset="utf-8">
<title>brightyearsahead.com</title>
<link href="https://fonts.googleapis.com/css2?family=Exo+2:wght@500;600;700&family=Lato:wght@400;700&display=swap" rel="stylesheet">
<style>
:root{
  --blue:#3ba3d8;
  --green:#2fad4b;
  --ink:#2b2b2b;
  --muted:#555;
  --line:#d9d9d9;
  --tag:#666;
  --white:#fff;
}
*{box-sizing:border-box;margin:0;padding:0}
html,body{width:1200px;height:2609px;overflow:hidden;background:var(--white)}
body{position:relative;font-family:"Lato",sans-serif;color:var(--ink)}
.abs{position:absolute}

/* header */
.follow{left:174px;top:14px;display:flex;align-items:center;gap:8px;font-size:13px;font-weight:700;color:#444}
.follow .dot{width:28px;height:28px;border-radius:50%;background:#5b5b5b}
.follow .dot:first-of-type{background:#3b5fa8}
.search{left:810px;top:10px;width:214px;height:32px;display:flex;border:1px solid #bbb;border-radius:3px;overflow:hidden}
.search span{flex:1;padding:7px 8px;font-size:12px;color:#999}
.search i{width:30px;background:var(--green);display:flex;align-items:center;justify-content:center}
.logo{left:169px;top:60px;font-family:"Exo 2",sans-serif;font-weight:600;font-size:30px;color:var(--blue);letter-spacing:.3px}
.nav{left:527px;top:74px;display:flex;gap:0;font-family:"Exo 2",sans-serif;font-weight:600;font-size:16px}
.nav a{color:var(--ink);text-decoration:none;position:absolute;white-space:nowrap}
.nav a.active{color:var(--green)}

/* hero */
.hero{left:0;top:117px;width:1200px;height:473px;background:linear-gradient(180deg,#7fb4e0 0%,#c5dcef 30%,#4c6a55 45%,#d9c9a8 70%,#c4a880 100%)}
.hero-caption{left:0;top:539px;width:1200px;height:51px;background:rgba(0,0,0,.55);color:#fff;font-family:"Exo 2",sans-serif;font-weight:600;font-size:22px;padding:11px 0 0 174px}
.arrow{top:318px;width:34px;height:32px;background:rgba(60,60,60,.8);display:flex;align-items:center;justify-content:center}

/* categories */
.cat{top:616px;width:277px;height:163px;border-radius:6px;display:flex;flex-direction:column;align-items:center;justify-content:center;gap:6px;color:#fff;font-family:"Exo 2",sans-serif;font-weight:700;font-size:22px}
.cat.feeling{left:172px;background:linear-gradient(160deg,#7f8d6a,#a8a57a 60%,#5f6a4a)}
.cat.fashion{left:463px;background:linear-gradient(180deg,#6a86a0,#8eaabf 55%,#b3a98e)}
.cat.fitness{left:751px;background:linear-gradient(180deg,#5d6f86,#7a8aa0 55%,#4f5a48)}
.cat .ic{width:40px;height:40px;border:3px solid #fff;border-radius:50%}

.section-title{left:0;width:1200px;top:852px;text-align:center;font-family:"Exo 2",sans-serif;font-weight:600;font-size:39px}

/* cards */
.card{width:280px;height:410px;border:1px solid var(--line);padding:7px 7px 0}
.thumb{height:195px}
.thumb.feeling{background:linear-gradient(180deg,#f2f2f2,#c9c9c9 75%,#5a5a5a)}
.thumb.fashion{background:linear-gradient(120deg,#3f6a3a,#8e9a8a 50%,#e8e8ee)}
.thumb.fitness{background:linear-gradient(180deg,#ffffff,#f3d9d4 60%,#c7a9a0)}
.tag{display:inline-block;margin-top:18px;height:24px;padding:3px 17px;font-family:"Exo 2",sans-serif;font-weight:700;font-size:14px;color:#fff;background:var(--tag)}
.tag.blue{background:var(--blue)}
.card h3{margin-top:12px;font-family:"Exo 2",sans-serif;font-weight:700;font-size:16.5px}
.by{margin-top:6px;font-size:10px;font-weight:700}
.excerpt{margin-top:10px;font-size:9.5px;line-height:17px;color:var(--muted)}
.share{margin-top:10px;display:flex;gap:2px;align-items:center;font-size:10px}
.share b{width:13px;height:13px;display:block}

/* load more */
.more{left:304px;top:2282px;width:592px;height:40px;border:1px solid #888;border-radius:4px;display:flex;align-items:center;justify-content:center;gap:8px;font-size:12px;color:#444}

/* newsletter */
.nl-title{left:0;width:1200px;top:2380px;text-align:center;font-family:"Exo 2",sans-serif;font-weight:600;font-size:34px}
.nl-sub{left:0;width:1200px;top:2427px;text-align:center;font-size:14px;color:#555}
.field{top:2478px;width:310px;height:44px;border:1px solid #ccc;border-radius:22px;padding:13px 0 0 24px;font-size:13px;font-weight:700;color:#333}
.submit{left:847px;top:2480px;width:130px;height:40px;border-radius:20px;background:var(--blue);color:#fff;font-family:"Exo 2",sans-serif;font-weight:700;font-size:16px;text-align:center;padding-top:9px}
.footer{left:0;top:2565px;width:1200px;height:44px;background:var(--green);color:#fff;font-size:13px;font-weight:700;text-align:center;padding-top:14px}
</style>
</head>
<body>

<div class="abs follow">Follow Us On <span class="dot"></span><span class="dot"></span><span class="dot"></span></div>
<div class="abs search"><span>Search here</span><i><svg width="14" height="14" viewBox="0 0 14 14"><circle cx="6" cy="6" r="4.2" fill="none" stroke="#fff" stroke-width="1.8"/><line x1="9" y1="9" x2="13" y2="13" stroke="#fff" stroke-width="1.8"/></svg></i></div>
<div class="abs logo">brightyearsahead.com</div>
<nav class="abs nav">
  <a class="active" style="left:0">Home</a>
  <a style="left:85px">Fashion</a>
  <a style="left:179px">Feeling</a>
  <a style="left:270px">Fitness</a>
  <a style="left:362px">About</a>
  <a style="left:447px">Contact</a>
</nav>

<div class="abs hero" role="img" aria-label="Beach scene with a couple relaxing in deck chairs and a surfer carrying a yellow board"></div>
<div class="abs hero-caption">Lorem Ipsum Dolor Sit Ametem Ipsum Dolor Sit Ame Ecit Adipi&nbsp; Consecit Adipi</div>
<div class="abs arrow" style="left:6px"><svg width="10" height="14"><path d="M8 2 3 7l5 5" stroke="#fff" stroke-width="2.5" fill="none"/></svg></div>
<div class="abs arrow" style="left:1157px"><svg width="10" height="14"><path d="M2 2l5 5-5 5" stroke="#fff" stroke-width="2.5" fill="none"/></svg></div>

<a class="abs cat feeling" role="img" aria-label="Woman with umbrella in a field"><span class="ic"></span>FEELING</a>
<a class="abs cat fashion" role="img" aria-label="Couple walking on a beach"><span class="ic"></span>FASHION</a>
<a class="abs cat fitness" role="img" aria-label="Woman doing a yoga pose outdoors"><span class="ic"></span>FITNESS</a>

<h2 class="abs section-title">All Posts in “Article List”</h2>

<!-- row 1 -->
<article class="abs card" style="left:172px;top:936px"><div class="thumb feeling" role="img" aria-label="Silhouette releasing a flock of birds"></div><span class="tag blue">FEELING</span><h3>Lorem ipsum consectetuer</h3><p class="by">By: Simply Dummy Text</p><p class="excerpt">Lorem ipsum dolor sit amete, consectetuer adipiscing elit, sed diam nonummy nibh euismod tincidunt utlaor dolore ma aliquam erat volutpat...[+]</p><div class="share"><b style="background:#2fad4b"></b><b style="background:#3b5fa8"></b><b style="background:#3ba3d8"></b><b style="background:#1f78b4"></b><b style="background:#d9463a"></b>&nbsp; 0</div></article>
<article class="abs card" style="left:461px;top:936px"><div class="thumb fashion" role="img" aria-label="Silver-haired woman in a scarf and blazer"></div><span class="tag">FASHION</span><h3>Lorem ipsum consectetuer</h3><p class="by">By: Simply Dummy Text</p><p class="excerpt">Lorem ipsum dolor sit amete, consectetuer adipiscing elit, sed diam nonummy nibh euismod tincidunt utlaor dolore ma aliquam erat volutpat...[+]</p><div class="share"><b style="background:#2fad4b"></b><b style="background:#3b5fa8"></b><b style="background:#3ba3d8"></b><b style="background:#1f78b4"></b><b style="background:#d9463a"></b>&nbsp; 0</div></article>
<article class="abs card" style="left:750px;top:936px"><div class="thumb fitness" role="img" aria-label="Group of older adults lifting dumbbells"></div><span class="tag">FITNESS</span><h3>Lorem ipsum consectetuer</h3><p class="by">By: Simply Dummy Text</p><p class="excerpt">Lorem ipsum dolor sit amete, consectetuer adipiscing elit, sed diam nonummy nibh euismod tincidunt utlaor dolore ma aliquam erat volutpat...[+]</p><div class="share"><b style="background:#2fad4b"></b><b style="background:#3b5fa8"></b><b style="background:#3ba3d8"></b><b style="background:#1f78b4"></b><b style="background:#d9463a"></b>&nbsp; 0</div></article>

<!-- row 2 -->
<article class="abs card" style="left:172px;top:1383px"><div class="thumb fitness" role="img" aria-label="Group of older adults lifting dumbbells"></div><span class="tag">FITNESS</span><h3>Lorem ipsum consectetuer</h3><p class="by">By: Simply Dummy Text</p><p class="excerpt">Lorem ipsum dolor sit amete, consectetuer adipiscing elit, sed diam nonummy nibh euismod tincidunt utlaor dolore ma aliquam erat volutpat...[+]</p><div class="share"><b style="background:#2fad4b"></b><b style="background:#3b5fa8"></b><b style="background:#3ba3d8"></b><b style="background:#1f78b4"></b><b style="background:#d9463a"></b>&nbsp; 0</div></article>
<article class="abs card" style="left:461px;top:1383px"><div class="thumb feeling" role="img" aria-label="Silhouette releasing a flock of birds"></div><span class="tag">FEELING</span><h3>Lorem ipsum consectetuer</h3><p class="by">By: Simply Dummy Text</p><p class="excerpt">Lorem ipsum dolor sit amete, consectetuer adipiscing elit, sed diam nonummy nibh euismod tincidunt utlaor dolore ma aliquam erat volutpat...[+]</p><div class="share"><b style="background:#2fad4b"></b><b style="background:#3b5fa8"></b><b style="background:#3ba3d8"></b><b style="background:#1f78b4"></b><b style="background:#d9463a"></b>&nbsp; 0</div></article>
<article class="abs card" style="left:750px;top:1383px"><div class="thumb fashion" role="img" aria-label="Silver-haired woman in a scarf and blazer"></div><span class="tag">FASHION</span><h3>Lorem ipsum consectetuer</h3><p class="by">By: Simply Dummy Text</p><p class="excerpt">Lorem ipsum dolor sit amete, consectetuer adipiscing elit, sed diam nonummy nibh euismod tincidunt utlaor dolore ma aliquam erat volutpat...[+]</p><div class="share"><b style="background:#2fad4b"></b><b style="background:#3b5fa8"></b><b style="background:#3ba3d8"></b><b style="background:#1f78b4"></b><b style="background:#d9463a"></b>&nbsp; 0</div></article>

<!-- row 3 -->
<article class="abs card" style="left:172px;top:1828px"><div class="thumb feeling" role="img" aria-label="Silhouette releasing a flock of birds"></div><span class="tag">FEELING</span><h3>Lorem ipsum consectetuer</h3><p class="by">By: Simply Dummy Text</p><p class="excerpt">Lorem ipsum dolor sit amete, consectetuer adipiscing elit, sed diam nonummy nibh euismod tincidunt utlaor dolore ma aliquam erat volutpat...[+]</p><div class="share"><b style="background:#2fad4b"></b><b style="background:#3b5fa8"></b><b style="background:#3ba3d8"></b><b style="background:#1f78b4"></b><b style="background:#d9463a"></b>&nbsp; 0</div></article>
<article class="abs card" style="left:461px;top:1828px"><div class="thumb fashion" role="img" aria-label="Silver-haired woman in a scarf and blazer"></div><span class="tag">FASHION</span><h3>Lorem ipsum consectetuer</h3><p class="by">By: Simply Dummy Text</p><p class="excerpt">Lorem ipsum dolor sit amete, consectetuer adipiscing elit, sed diam nonummy nibh euismod tincidunt utlaor dolore ma aliquam erat volutpat...[+]</p><div class="share"><b style="background:#2fad4b"></b><b style="background:#3b5fa8"></b><b style="background:#3ba3d8"></b><b style="background:#1f78b4"></b><b style="background:#d9463a"></b>&nbsp; 0</div></article>
<article class="abs card" style="left:750px;top:1828px"><div class="thumb fitness" role="img" aria-label="Group of older adults lifting dumbbells"></div><span class="tag">FITNESS</span><h3>Lorem ipsum consectetuer</h3><p class="by">By: Simply Dummy Text</p><p class="excerpt">Lorem ipsum dolor sit amete, consectetuer adipiscing elit, sed diam nonummy nibh euismod tincidunt utlaor dolore ma aliquam erat volutpat...[+]</p><div class="share"><b style="background:#2fad4b"></b><b style="background:#3b5fa8"></b><b style="background:#3ba3d8"></b><b style="background:#1f78b4"></b><b style="background:#d9463a"></b>&nbsp; 0</div></article>

<div class="abs more"><svg width="16" height="16" viewBox="0 0 16 16"><circle cx="8" cy="8" r="5.5" fill="none" stroke="#888" stroke-width="1.5" stroke-dasharray="2 2"/></svg>Load more blog</div>

<h2 class="abs nl-title">Newsletter Subscription</h2>
<p class="abs nl-sub">Subscribe to Our Newsletter to Get Latest Updates &amp; News About Us.</p>
<div class="abs field" style="left:212px">Enter Your Name:</div>
<div class="abs field" style="left:529px">Enter Your Email:</div>
<div class="abs submit">SUBMIT</div>

<footer class="abs footer">© 2018 brightyearsahead.com .All Rights Reserved.</footer>
</body>
</html>
```